Trifold Business Brochure Design Project

Can you design a trifold brochure for my business? Suggested material for each of the 6 panels is in the attached document, My logo is also attached (from print haven), and info on my website, derek@dereklhcpa.com. Colors to match my logo. Theme the same as my logo, an outdoor/mountain/river, etc feel.

Target Market(s)

Business owners

Requirements
Nice to have
• See attached

```html
<!DOCTYPE html>
<html lang="en">
<head>
<meta charset="utf-8">
<title>Derek Lindhart CPA – Trifold Brochure</title>
<link rel="stylesheet" href="https://fonts.googleapis.com/css2?family=Merriweather:wght@700&family=Lato:wght@400;700&family=Montserrat:wght@400;500&display=swap">
<style>
  :root{
    --page:#f1f5e8;
    --white:#ffffff;
    --pale:#f6f8ef;
    --lime:#bfdc69;
    --leaf:#a3c26a;
    --olive:#7b8a55;
    --forest:#3e5a43;
    --ink:#1f2d1a;
    --heading:#3e5a43;
    --tag:#8b9a5c;
  }
  *{margin:0;padding:0;box-sizing:border-box}
  html,body{width:1200px;height:486px;overflow:hidden;background:var(--page)}
  body{position:relative;font-family:"Lato",sans-serif;color:var(--ink)}
  .sheet{position:absolute;top:27px;width:562px;height:434px;overflow:hidden;background:var(--white);box-shadow:0 1px 4px rgba(0,0,0,.12)}
  .sheet--outside{left:22px}
  .sheet--inside{left:609px}
  .shapes{position:absolute;inset:0;width:562px;height:434px}
  .abs{position:absolute}
  .accent-bar{position:absolute;width:3px;background:var(--lime)}
  .serif{font-family:"Merriweather",serif;font-weight:700}
  .about-title{left:31px;top:122px;font-size:19.5px;line-height:29px;color:var(--heading)}
  .tagline{font-family:"Montserrat",sans-serif;font-size:5.6px;letter-spacing:.6px;color:var(--tag);text-transform:uppercase}
  .about-tag{left:30px;top:185px}
  .body-copy{font-size:8.1px;line-height:17px}
  .about-body{left:13px;top:208px;width:165px}
  .about-body p+p{margin-top:17px}
  .address-title{left:218px;top:24px;font-size:19px;color:var(--white)}
  .contact-list{left:203px;top:64px;list-style:none}
  .contact-list li{display:flex;align-items:center;height:30px;font-family:"Montserrat",sans-serif;font-size:10px;color:var(--white)}
  .contact-list svg{width:17px;height:17px;margin-right:10px;flex:none}
  .brand{left:374px;width:188px;top:260px;text-align:center}
  .brand-name{font-size:15.5px;color:var(--heading);white-space:nowrap}
  .services-title{left:32px;top:134px;font-size:19px;line-height:29px;color:var(--heading)}
  .service-list{list-style:none;font-weight:700;font-size:10px;color:var(--ink)}
  .service-list--a{left:13px;top:240px}
  .service-list--a li{height:34px}
  .service-list--b{left:203px;top:131px;width:150px}
  .service-list--b li{line-height:21px;margin-bottom:14px}
  .benefits-title{left:405px;top:79px;font-size:19.5px;line-height:29px;color:var(--white)}
  .benefits-body{left:388px;top:148px;width:170px;color:var(--white)}
  .benefits-body p+p{margin-top:17px}
</style>
</head>
<body>

<section class="sheet sheet--outside" aria-label="Brochure outside">
  <svg class="shapes" viewBox="0 0 562 434" aria-hidden="true">
    <rect x="187" y="0" width="187" height="434" fill="var(--olive)"/>
    <rect x="374" y="0" width="188" height="434" fill="var(--forest)"/>
    <polygon points="0,0 95,0 0,62" fill="var(--leaf)"/>
    <polygon points="29,42 95,0 169,119" fill="var(--lime)"/>
    <polygon points="468,56 562,118 562,313 493,358 374,286 374,118" fill="var(--white)"/>
    <polygon points="374,434 562,313 562,434" fill="var(--leaf)"/>
    <polygon points="216,188 493,358 374,434" fill="var(--lime)"/>
    <circle cx="468" cy="165" r="24" fill="var(--lime)"/>
  </svg>

  <div class="accent-bar" style="left:15px;top:125px;height:67px"></div>
  <h2 class="abs serif about-title">About Derek<br>Lindhart CPA</h2>
  <p class="abs tagline about-tag">Clear numbers for growing businesses</p>
  <div class="abs body-copy about-body">
    <p>At vero eos et accusamus et iusto odio dignissimos ducimus qui blanditiis praesentium voluptatum deleniti atque corrupti quos dolores et quas molestias excepturi sint occaecati cupiditate non provident, similique sunt in culpa qui officia.</p>
    <p>Nam libero tempore, cum soluta nobis est eligendi optio cumque nihil impedit quo minus id quod maxime placeat facere possimus, omnis voluptas assumenda est, omnis dolor repellendus.</p>
  </div>

  <div class="accent-bar" style="left:203px;top:23px;height:28px"></div>
  <h2 class="abs serif address-title">Address</h2>
  <ul class="abs contact-list">
    <li><svg viewBox="0 0 20 20"><circle cx="10" cy="10" r="10" fill="#fff"/><path d="M10 4.5a3.5 3.5 0 0 0-3.5 3.5c0 2.6 3.5 7 3.5 7s3.5-4.4 3.5-7A3.5 3.5 0 0 0 10 4.5z" fill="var(--olive)"/><circle cx="10" cy="8" r="1.3" fill="#fff"/></svg>PO Box 12, Pinecrest, OR 97000</li>
    <li><svg viewBox="0 0 20 20"><circle cx="10" cy="10" r="10" fill="#fff"/><path d="M7 5.5l1.6 2.2-1 1.1c.7 1.4 1.7 2.4 3.1 3.1l1.1-1 2.2 1.6-.8 1.8c-3.6-.4-6.6-3.4-7-7z" fill="var(--olive)"/></svg>555.014.2290</li>
    <li><svg viewBox="0 0 20 20"><circle cx="10" cy="10" r="10" fill="#fff"/><rect x="5.5" y="7" width="9" height="6.5" rx=".8" fill="var(--olive)"/><path d="M5.8 7.3L10 10.5l4.2-3.2" stroke="#fff" stroke-width=".8" fill="none"/></svg>derek@dereklhcpa.com</li>
    <li><svg viewBox="0 0 20 20"><circle cx="10" cy="10" r="10" fill="#fff"/><g fill="none" stroke="var(--olive)" stroke-width=".8"><circle cx="10" cy="10" r="4.5"/><ellipse cx="10" cy="10" rx="2" ry="4.5"/><path d="M5.5 10h9M6.2 7.8h7.6M6.2 12.2h7.6"/></g></svg>https://dereklhcpa.com</li>
  </ul>

  <div class="abs brand">
    <div class="serif brand-name">Derek Lindhart CPA</div>
  </div>
</section>

<section class="sheet sheet--inside" aria-label="Brochure inside">
  <svg class="shapes" viewBox="0 0 562 434">
    <defs>
      <linearGradient id="warmPhoto" x1="0" y1="0" x2="1" y2="1">
        <stop offset="0" stop-color="#e9e2d6"/><stop offset=".5" stop-color="#b67a52"/><stop offset="1" stop-color="#d8cfc2"/>
      </linearGradient>
      <linearGradient id="officePhoto" x1="0" y1="0" x2="1" y2="1">
        <stop offset="0" stop-color="#3c4a5a"/><stop offset=".5" stop-color="#6f7f93"/><stop offset="1" stop-color="#1e2835"/>
      </linearGradient>
    </defs>
    <rect x="187" y="0" width="187" height="434" fill="var(--pale)" aria-hidden="true"/>
    <polygon points="0,0 90,0 0,60" fill="var(--leaf)" aria-hidden="true"/>
    <polygon points="39,35 90,0 155,111" fill="var(--lime)" aria-hidden="true"/>
    <polygon points="90,0 562,0 174,122 155,111" fill="url(#warmPhoto)" role="img" aria-label="Photo of colleagues joining fists in teamwork"/>
    <polygon points="374,69 562,1 562,376 374,307" fill="var(--olive)" aria-hidden="true"/>
    <polygon points="360,316 562,376 562,434 281,434" fill="url(#officePhoto)" role="img" aria-label="Photo of two professionals smiling at a laptop"/>
    <polygon points="188,372 360,316 281,434" fill="var(--lime)" aria-hidden="true"/>
    <polygon points="188,372 281,434 188,434" fill="var(--leaf)" aria-hidden="true"/>
  </svg>

  <div class="accent-bar" style="left:17px;top:137px;height:77px"></div>
  <h2 class="abs serif services-title">Quality &amp; Timely<br>Financial<br>Services</h2>
  <ol class="abs service-list service-list--a">
    <li>1)&nbsp; Fractional CFO/Controller Services</li>
    <li>2)&nbsp; Financial/Cash Flow Projections</li>
    <li>3)&nbsp; Business Exit Planning</li>
    <li>4)&nbsp; Business Value Creation</li>
    <li>5)&nbsp; Industry KPIs &amp; Benchmarking</li>
  </ol>
  <ol class="abs service-list service-list--b">
    <li>6)&nbsp; Labor Analysis</li>
    <li>7)&nbsp; Tax Planning</li>
    <li>8)&nbsp; Internal Control/Audit Consulting</li>
    <li>9)&nbsp; System Conversions</li>
    <li>10)&nbsp; Accounting Services</li>
  </ol>

  <div class="accent-bar" style="left:389px;top:80px;height:55px"></div>
  <h2 class="abs serif benefits-title">Our<br>Benefits</h2>
  <div class="abs body-copy benefits-body">
    <p>Nam libero tempore, cum soluta nobis est eligendi optio cumque nihil impedit quo minus id quod maxime placeat facere possimus, omnis voluptas assumenda est, omnis dolor repellendus.</p>
    <p>Temporibus autem quibusdam et aut officiis debitis aut rerum necessitatibus saepe eveniet sint et molestiae non recusandae.</p>
  </div>
</section>

</body>
</html>
```